Alcohol designs Birthday Sign's needs more templates

We are after 10 new designs for signable custom birthday signs, alcohol theme inspired (beer, wine, spirits) for this batch, You do not need to provide 10 designs however the winner will be based on final look and quantity.
For example someone may win with one design or ten designs. We will also look at purchasing more individual designs for any winners or potential winners. Designs must be in layers, CMYK, 8bits channel, saved as TIFF or PDS or AI, size is 460mm wide x by 1060mm high with 30mm bleed included, total graphic size will be 430 x 1030 at 300ppi, any text must be editable and font files included. see attached for sample's, signable area needs to be on each design and a sample persons name, other then that we a excited to see what everyone comes up with
Reason: Allow more designs to be supplied form current designers and new designers. Also to allow us to choose more than one designer by adding a second/third place
Birthday
- Layers.
- Space for people to sign
- At least 3 designs (These can be of the same template you design just with a small them change beer, wine etc)

```html
<!DOCTYPE html>
<html lang="en">
<head>
<meta charset="utf-8">
<title>Don't Whine Just Wine – Birthday Sign</title>
<link rel="stylesheet" href="https://fonts.googleapis.com/css2?family=Playfair+Display:wght@400;700;900&display=swap">
<style>
  :root {
    --ink: #0b0b0b;
    --paper: #ffffff;
    --rose-pale: #f8d9e4;
    --rose-soft: #f2a9c4;
    --rose: #e45a91;
    --magenta: #e0307a;
    --wine: #c41f5a;
    --berry: #a52a45;
  }
  html, body {
    margin: 0;
    padding: 0;
    overflow: hidden;
    background: var(--paper);
  }
  .sign {
    position: relative;
    width: 1200px;
    height: 2761px;
    overflow: hidden;
    background: var(--paper);
    font-family: "Playfair Display", Georgia, serif;
    color: var(--ink);
  }
  .wash {
    position: absolute;
    inset: 0;
    width: 1200px;
    height: 2761px;
  }
  .glass-art {
    position: absolute;
    left: 762px;
    top: 160px;
    width: 322px;
    height: 1212px;
  }
  .headline {
    position: absolute;
    right: 469px;
    margin: 0;
    font-weight: 900;
    font-size: 170px;
    line-height: 1;
    letter-spacing: -2px;
    text-align: right;
    white-space: nowrap;
  }
  .headline--1 { top: 677px; }
  .headline--2 { top: 855px; }
  .headline--3 { top: 1031px; }
  .headline--4 { top: 1207px; }
  .cheer {
    position: absolute;
    left: 0;
    width: 1160px;
    margin: 0;
    text-align: center;
    line-height: 1;
    white-space: nowrap;
  }
  .cheer--sip {
    top: 1552px;
    font-size: 112px;
    font-weight: 400;
    color: var(--rose);
    letter-spacing: 1px;
  }
  .cheer--hooray {
    top: 1712px;
    font-size: 150px;
    font-weight: 700;
    color: var(--magenta);
  }
  .cheer__bang { color: var(--berry); }
  .celebrant {
    position: absolute;
    left: 0;
    width: 1200px;
    margin: 0;
    text-align: center;
    line-height: 1;
    white-space: nowrap;
  }
  .celebrant--intro { top: 2173px; font-size: 95px; font-weight: 400; }
  .celebrant--name { top: 2306px; font-size: 100px; font-weight: 900; }
  .celebrant--occasion { top: 2475px; font-size: 118px; font-weight: 400; letter-spacing: 2px; }
  .rule {
    position: absolute;
    left: 200px;
    width: 800px;
    height: 4px;
    background: var(--ink);
  }
  .rule--top { top: 2461px; }
  .rule--bottom { top: 2609px; }
</style>
</head>
<body>
<main class="sign">
  <svg class="wash" viewBox="0 0 1200 2761" role="img" aria-label="Soft pink watercolour wash decoration framing the sign">
    <defs>
      <filter id="soften" x="-20%" y="-20%" width="140%" height="140%">
        <feGaussianBlur stdDeviation="30"/>
      </filter>
      <radialGradient id="wash-top-left" cx="0.2" cy="0.4" r="0.8">
        <stop offset="0" stop-color="#ef8fb4" stop-opacity="0.85"/>
        <stop offset="1" stop-color="#f8d9e4" stop-opacity="0"/>
      </radialGradient>
      <radialGradient id="wash-bottom" cx="0.8" cy="0.6" r="0.8">
        <stop offset="0" stop-color="#e8629a" stop-opacity="0.9"/>
        <stop offset="0.6" stop-color="#f4b3cb" stop-opacity="0.6"/>
        <stop offset="1" stop-color="#fbe4ec" stop-opacity="0"/>
      </radialGradient>
    </defs>
    <g filter="url(#soften)">
      <ellipse cx="90" cy="520" rx="260" ry="560" fill="url(#wash-top-left)"/>
      <ellipse cx="600" cy="20" rx="620" ry="130" fill="#f8d6e2" opacity="0.8"/>
      <ellipse cx="1160" cy="260" rx="120" ry="320" fill="#f6c6d7" opacity="0.7"/>
      <ellipse cx="1040" cy="2000" rx="360" ry="620" fill="url(#wash-bottom)"/>
      <ellipse cx="600" cy="2700" rx="720" ry="260" fill="url(#wash-bottom)"/>
      <ellipse cx="80" cy="2500" rx="220" ry="380" fill="#f6c0d3" opacity="0.7"/>
    </g>
  </svg>

  <svg class="glass-art" viewBox="0 0 322 1212" role="img" aria-label="Watercolour illustration of a wine glass with red wine splashing out of it">
    <defs>
      <linearGradient id="glass-tone" x1="0" y1="0" x2="0" y2="1">
        <stop offset="0" stop-color="#f3b6cb"/>
        <stop offset="0.45" stop-color="#d33a70"/>
        <stop offset="1" stop-color="#e784aa"/>
      </linearGradient>
    </defs>
    <rect x="0" y="0" width="322" height="1212" rx="60" fill="url(#glass-tone)" opacity="0.85"/>
  </svg>

  <h1 class="headline headline--1">DONT</h1>
  <p class="headline headline--2">WHINE</p>
  <p class="headline headline--3">JUST</p>
  <p class="headline headline--4">WINE</p>

  <p class="cheer cheer--sip">SIPP..... SIPP.....</p>
  <p class="cheer cheer--hooray">HOORAY <span class="cheer__bang">!!!</span></p>

  <p class="celebrant celebrant--intro">It’s</p>
  <p class="celebrant celebrant--name">Oliver</p>
  <div class="rule rule--top"></div>
  <p class="celebrant celebrant--occasion">BIRTHDAY</p>
  <div class="rule rule--bottom"></div>
</main>
</body>
</html>
```